Verdant Medispa Business Card

need a business card for our medispa, attached please see the logo.
our website is https://verdantmedispa-example.com

Sorina Belcourt, MD
Internal Medicine

555-204-7193

Sorina@verdantmedispa-example.com

Www.Verdantmedispa-example.com

738 E Harlow Blvd N, Ste 512, Katy, TX 77981

Target Market(s)

MedSpa, Cosmetics, Esthetics

Industry/Entity Type

MedicalSpa

Contact Information for Business Card

Please see the attached business card which i pulled from the internet. I like the idea back as a logo and front with info.

Font styles to use
Decorative

Requirements
Must have
• Color should be matching with Logo and Website theme, Also I like to have QR code for the website

```html
<!DOCTYPE html>
<html lang="en">
<head>
<meta charset="utf-8">
<title>Verdant Medispa Business Card</title>
<link href="https://fonts.googleapis.com/css2?family=Cinzel:wght@400&family=Poppins:wght@400;500&display=swap" rel="stylesheet">
<style>
  :root {
    --backdrop: #cbcbcb;
    --paper: #ffffff;
    --cocoa: #7b6652;
    --gold: #d6b03a;
    --ink: #5e4d3e;
  }
  * { margin: 0; padding: 0; box-sizing: border-box; }
  html, body { width: 1200px; height: 1200px; overflow: hidden; }
  body { background: var(--backdrop); position: relative; font-family: "Poppins", sans-serif; }

  .card {
    position: absolute;
    left: 218px;
    width: 765px;
    height: 436px;
    border-radius: 62px;
    overflow: hidden;
    box-shadow: 0 14px 34px rgba(0,0,0,0.28);
  }
  .card--front { top: 124px; background: var(--paper); }
  .card--back { top: 640px; background: var(--cocoa); }

  .wordmark {
    position: absolute;
    left: 0; right: 0;
    text-align: center;
    font-family: "Cinzel", serif;
    font-weight: 400;
    color: var(--gold);
    white-space: nowrap;
  }
  .card--front .wordmark { top: 68px; font-size: 44px; letter-spacing: 2px; }
  .card--back .wordmark { top: 190px; font-size: 64px; letter-spacing: 3px; }

  .holder {
    position: absolute;
    right: 410px;
    top: 240px;
    text-align: right;
    white-space: nowrap;
  }
  .holder__name {
    font-family: "Cinzel", serif;
    font-weight: 400;
    font-size: 26px;
    color: var(--gold);
    letter-spacing: 0.3px;
    line-height: 1.2;
  }
  .holder__role {
    font-size: 23px;
    font-weight: 500;
    color: var(--cocoa);
    margin-top: 4px;
    line-height: 1.2;
  }

  .divider {
    position: absolute;
    left: 381px;
    top: 188px;
    width: 3px;
    height: 180px;
    border-radius: 2px;
    background: var(--cocoa);
  }

  .contacts {
    position: absolute;
    left: 425px;
    top: 204px;
    list-style: none;
  }
  .contacts__item {
    display: flex;
    align-items: flex-start;
    font-size: 14.5px;
    color: var(--ink);
    line-height: 24px;
    margin-bottom: 15px;
    white-space: nowrap;
  }
  .contacts__icon { width: 23px; height: 23px; flex: none; margin-right: 14px; margin-top: 1px; }

  .wave { position: absolute; left: 0; top: 0; width: 765px; height: 436px; }

  .qr-code {
    position: absolute;
    right: 56px;
    bottom: 44px;
    width: 84px;
    height: 84px;
    border-radius: 6px;
    background: var(--paper);
    border: 3px solid var(--gold);
  }
</style>
</head>
<body>

<section class="card card--front">
  <svg class="wave" viewBox="0 0 765 436" aria-hidden="true">
    <path d="M0,390 C60,372 100,366 140,366 C250,366 420,420 640,436 L0,436 Z" fill="var(--cocoa)"/>
    <path d="M276,372 C420,400 560,422 650,425 C700,426 745,415 752,392 C740,412 700,419 650,419 C560,417 420,397 276,372 Z" fill="var(--gold)"/>
  </svg>

  <div class="wordmark">Verdant Medispa</div>

  <div class="holder">
    <h1 class="holder__name">Sorina Belcourt, MD</h1>
    <p class="holder__role">Internal Medicine</p>
  </div>

  <div class="divider"></div>

  <ul class="contacts">
    <li class="contacts__item">
      <svg class="contacts__icon" viewBox="0 0 24 24" aria-hidden="true">
        <circle cx="12" cy="12" r="12" fill="var(--gold)"/>
        <path d="M8.2 6.5l2 2.6-1.2 1.3c.7 1.6 1.9 2.8 3.5 3.5l1.3-1.2 2.6 2-1.3 1.9c-3.9-.5-7.5-4.1-8-8z" fill="#fff"/>
      </svg>
      <span>555-204-7193</span>
    </li>
    <li class="contacts__item">
      <svg class="contacts__icon" viewBox="0 0 24 24" aria-hidden="true">
        <circle cx="12" cy="12" r="12" fill="var(--gold)"/>
        <rect x="6" y="8" width="12" height="8.5" rx="1" fill="none" stroke="#fff" stroke-width="1.5"/>
        <path d="M6.5 8.5l5.5 4.3 5.5-4.3M6.5 16l4-3.5M17.5 16l-4-3.5" fill="none" stroke="#fff" stroke-width="1.3"/>
      </svg>
      <span>Sorina@verdantmedispa-example.com</span>
    </li>
    <li class="contacts__item">
      <svg class="contacts__icon" viewBox="0 0 24 24" aria-hidden="true">
        <circle cx="12" cy="12" r="12" fill="var(--gold)"/>
        <g fill="none" stroke="#fff" stroke-width="1.3">
          <circle cx="12" cy="12" r="6"/>
          <ellipse cx="12" cy="12" rx="2.6" ry="6"/>
          <path d="M6 12h12"/>
        </g>
      </svg>
      <span>Www.Verdantmedispa-example.com</span>
    </li>
    <li class="contacts__item">
      <svg class="contacts__icon" viewBox="0 0 24 24" aria-hidden="true">
        <circle cx="12" cy="12" r="12" fill="var(--gold)"/>
        <path d="M12 5.5a4.5 4.5 0 0 0-4.5 4.5c0 3.3 4.5 8.3 4.5 8.3s4.5-5 4.5-8.3A4.5 4.5 0 0 0 12 5.5z" fill="#fff"/>
        <circle cx="12" cy="10" r="1.7" fill="var(--gold)"/>
      </svg>
      <span>738 E Harlow Blvd N, Ste 512, Katy,<br>TX 77981</span>
    </li>
  </ul>
</section>

<section class="card card--back">
  <div class="wordmark">Verdant Medispa</div>
  <div class="qr-code" role="img" aria-label="QR code linking to the Verdant Medispa website"></div>
</section>

</body>
</html>
```